KALVENTA Branded Wellness Pouch Design for Clinical Study Kit

Overview:
We are creating custom zippered pouches for our “KALVENTA Trial Spark Packs,” which will be distributed to physicians, nurses, and research coordinators participating in a national clinical study. We need a clean, professional design for the front of the pouch that incorporates our existing KALVENTA logo and the new supporting text.
Design Requirements:
Keep the existing KALVENTA logo intact (we’ll upload the file).
Add the text “Trial Spark Pack” immediately following the logo, using the same or a complementary font.
Add a tagline below that reads:
Recharge. Kalventa. Rise.
Use a layout that looks balanced, legible, and polished when printed on a small pouch.
Stay consistent with our brand color palette (blue from the logo)
The overall style should feel modern, wellness-driven, and professional — think premium, science-forward, and sleek.
Audience:
This kit will be given to medical professionals, so the design should feel elevated and credible (not flashy or overly playful).
Deliverables:
Vector file (AI, EPS)
It is a frosted white, zippered vinyl pouch (9 1/2 " x 8 1/4 " x 2 1/2 ")
The imprint size is (6 3/4" W x 4 1/2" H)
The imprint can only be 1-color, so in this case - we would like the color to be the dark blue (#06173c)

```html
<!DOCTYPE html>
<html lang="en">
<head>
<meta charset="utf-8">
<title>KALVENTA Trial Spark Pack</title>
<link rel="stylesheet" href="https://fonts.googleapis.com/css2?family=Bebas+Neue&family=Saira+Extra+Condensed:wght@600&display=swap">
<style>
  :root {
    --imprint: #06173c;
    --paper: #ffffff;
  }
  html, body {
    margin: 0;
    padding: 0;
    width: 1200px;
    height: 800px;
    overflow: hidden;
    background: var(--paper);
  }
  .pouch-front {
    display: block;
    width: 1200px;
    height: 800px;
  }
  .brand-mark { fill: var(--imprint); }
  .brand-name {
    font-family: "Bebas Neue", "Oswald", sans-serif;
    font-size: 156px;
    fill: var(--imprint);
  }
  .trial-descriptor {
    font-family: "Saira Extra Condensed", "Arial Narrow", sans-serif;
    font-weight: 600;
    font-size: 24px;
    fill: var(--imprint);
  }
  .kit-name {
    font-family: "Bebas Neue", "Oswald", sans-serif;
    font-size: 66px;
    fill: var(--imprint);
  }
  .tagline-line {
    font-family: "Bebas Neue", "Oswald", sans-serif;
    font-size: 76px;
    fill: none;
    stroke: var(--imprint);
    stroke-width: 1.6;
    letter-spacing: 1px;
  }
</style>
</head>
<body>
<svg class="pouch-front" viewBox="0 0 1200 800" xmlns="http://www.w3.org/2000/svg" aria-labelledby="pouch-title">
  <title id="pouch-title">KALVENTA U.S. Trial Spark Pack – Recharge. Kalventa. Rise.</title>

  <g class="logo-lockup">
    <rect class="brand-mark" x="236" y="150" width="72" height="72"/>
    <text class="brand-name" x="334" y="240" textLength="634" lengthAdjust="spacingAndGlyphs">KALVENTA U.S.</text>
    <text class="trial-descriptor" x="334" y="275" textLength="634" lengthAdjust="spacingAndGlyphs">Lumora Disc NP Randomized, Sham-Controlled, Multi-Center, Double Blind Clinical Trial</text>
    <text class="kit-name" x="968" y="347" text-anchor="end">TRIAL SPARK PACK</text>
  </g>

  <g class="tagline">
    <text class="tagline-line" x="240" y="552">RECHARGE.</text>
    <text class="tagline-line" x="240" y="622">KALVENTA.</text>
    <text class="tagline-line" x="240" y="694">RISE.</text>
  </g>
</svg>
</body>
</html>
```